Marnie's Hideaway Flyer

Need an attractive flyer for an existing Spa in SG around the Larkview area ( Former Meadow Hall) . Our spa is s converted horse stables , environment totally back to nature - see horse riding etc...even though it is located in the suburbs
Main business come from facials, waxing/hair removals, instant spraytan and body works. Flyer needs to attract new clients to our business.
Updates

I have done some updates on my requirements.

Target Market(s)

Adults of 25 -65 ( male and female), English speaking

Industry/Entity Type

Environment

Font styles to use
Script

Requirements
Must have
• Must have the 5 logos of the top brand products we use in the Spa.
Should not have
• No tacky designs. Must maintain class and decorum .
No animations too.

```html
<!DOCTYPE html>
<html lang="en">
<head>
<meta charset="utf-8">
<title>Marnie's Hideaway Flyer</title>
<link rel="stylesheet" href="https://fonts.googleapis.com/css2?family=Arimo:wght@400;700&family=Crimson+Text:wght@400;700&family=Kaushan+Script&family=Roboto+Slab:wght@700&display=swap">
<style>
  :root {
    --wine-deep: #3a0508;
    --wine: #6e0b10;
    --red: #d01218;
    --red-dark: #a40c11;
    --silver-light: #ffffff;
    --silver: #dcdcdc;
    --silver-dark: #b9b9b9;
    --ink: #2a2a2a;
    --white: #ffffff;
  }
  * { box-sizing: border-box; margin: 0; padding: 0; }
  html, body { width: 904px; height: 1200px; overflow: hidden; background: #f2f2f2; }
  .flyer { position: relative; width: 904px; height: 1200px; overflow: hidden; font-family: "Arimo", sans-serif; }
  .backdrop { position: absolute; inset: 0; }

  .photo { position: absolute; }
  .photo-roses { left: 230px; top: 205px; width: 270px; height: 230px; border-radius: 50%;
    background: radial-gradient(circle at 45% 45%, #e0191d 0%, #a70a10 45%, rgba(80,5,8,0) 72%); }
  .photo-hero { left: 652px; top: 0; width: 252px; height: 360px;
    background: linear-gradient(160deg, #e9d0c2 0%, #d9b3a0 50%, #8a3a30 100%); }

  .nav { position: absolute; top: 40px; left: 0; width: 652px; height: 48px;
    background: linear-gradient(90deg, rgba(160,12,17,.55), rgba(160,12,17,.2)); }
  .nav-item { position: absolute; top: 6px; font-family: "Kaushan Script", cursive; font-size: 24px; color: var(--white); white-space: nowrap; }

  .intro { position: absolute; left: 16px; top: 116px; width: 630px; font-family: "Crimson Text", serif;
    font-size: 24px; line-height: 31px; color: var(--white); }

  .service-circle { position: absolute; border-radius: 50%; border: 8px solid var(--white);
    box-shadow: 0 0 0 3px #9a9a9a, 0 6px 14px rgba(0,0,0,.35); }
  .circle-waxing { left: 42px; top: 312px; width: 302px; height: 302px;
    background: linear-gradient(160deg, #f4f1ee, #dcc2b2 60%, #c9a391); }
  .circle-nails { left: 370px; top: 512px; width: 274px; height: 274px;
    background: linear-gradient(150deg, #7fa9b6, #e4c8b8 45%, #f3ece7); }
  .circle-facial { left: 648px; top: 672px; width: 230px; height: 230px;
    background: linear-gradient(170deg, #eeeeee, #e6cfc2 55%, #b98d7a); }

  .brand-name { position: absolute; right: 14px; top: 438px; font-family: "Arimo", sans-serif;
    font-size: 50px; font-weight: 400; color: var(--ink); letter-spacing: -0.5px; white-space: nowrap; }

  .open-daily { position: absolute; left: 26px; top: 672px; font-family: "Roboto Slab", serif;
    font-size: 26px; color: var(--red); }
  .call-in { position: absolute; left: 26px; top: 710px; font-size: 34px; line-height: 44px; color: var(--ink); }

  .web-pill { position: absolute; left: 0; top: 866px; width: 462px; height: 68px;
    border-radius: 0 20px 20px 0; background: linear-gradient(180deg, #e0191f, var(--red-dark));
    box-shadow: 0 3px 8px rgba(0,0,0,.3); color: var(--white); font-size: 32px; font-weight: 700;
    padding: 14px 0 0 26px; white-space: nowrap; }

  .partners { position: absolute; top: 984px; left: 0; width: 904px; }
  .partner { position: absolute; top: 0; font-family: "Arimo", sans-serif; font-size: 22px; font-weight: 700;
    color: #444; white-space: nowrap; }

  .address { position: absolute; left: 14px; top: 1012px; font-family: "Crimson Text", serif; font-size: 16px;
    line-height: 20px; color: var(--white); font-style: normal; }
  .footer-url { position: absolute; left: 420px; top: 1138px; font-family: "Crimson Text", serif; font-size: 36px;
    font-weight: 700; color: var(--white); white-space: nowrap; }
</style>
</head>
<body>
<main class="flyer">
  <svg class="backdrop" width="904" height="1200" viewBox="0 0 904 1200" aria-hidden="true">
    <defs>
      <linearGradient id="wine-fill" x1="0" y1="0" x2="0" y2="1">
        <stop offset="0" stop-color="#5a080c"/>
        <stop offset="0.6" stop-color="var(--wine)"/>
        <stop offset="1" stop-color="var(--wine-deep)"/>
      </linearGradient>
      <linearGradient id="silver-fill" x1="0" y1="0" x2="0" y2="1">
        <stop offset="0" stop-color="var(--silver-light)"/>
        <stop offset="0.5" stop-color="var(--silver)"/>
        <stop offset="1" stop-color="var(--silver-dark)"/>
      </linearGradient>
      <linearGradient id="red-fill" x1="0" y1="0" x2="0" y2="1">
        <stop offset="0" stop-color="#e3161c"/>
        <stop offset="1" stop-color="var(--red-dark)"/>
      </linearGradient>
    </defs>
    <rect x="0" y="0" width="904" height="480" fill="url(#wine-fill)"/>
    <path d="M0,455 C200,470 380,440 560,380 C680,340 800,330 904,335 L904,1200 L0,1200 Z" fill="url(#silver-fill)"/>
    <path d="M560,384 C680,344 800,331 904,335 L904,402 C820,382 720,386 620,406 Z" fill="url(#red-fill)"/>
    <path d="M0,352 C40,360 80,372 124,392 L124,400 C80,386 40,378 0,378 Z" fill="var(--red)"/>
    <path d="M150,1200 C250,1138 380,1096 560,1086 C720,1078 820,1074 904,1068 L904,1200 Z" fill="var(--white)"/>
    <path d="M170,1200 C260,1150 380,1110 560,1100 C720,1092 820,1090 904,1085 L904,1200 Z" fill="url(#red-fill)"/>
    <path d="M0,986 C60,972 110,956 154,950 C180,1000 194,1100 206,1200 L0,1200 Z" fill="#9c9c9c"/>
    <path d="M0,992 C60,978 108,962 148,957 C172,1004 184,1100 194,1200 L0,1200 Z" fill="url(#red-fill)"/>
  </svg>

  <div class="photo photo-roses" role="img" aria-label="Large red rose on a bed of dark roses"></div>
  <div class="photo photo-hero" role="img" aria-label="Portrait of a woman with glowing skin touching her cheeks"></div>

  <nav class="nav">
    <span class="nav-item" style="left:16px">Waxing</span>
    <span class="nav-item" style="left:193px">Nails</span>
    <span class="nav-item" style="left:322px">Spraytan</span>
    <span class="nav-item" style="left:452px">Face</span>
    <span class="nav-item" style="left:578px">Body</span>
  </nav>

  <p class="intro">Looking and feeling good doesn't need to be your little secret.<br>From Facials, Brazilian waxing to nails and body,<br>Marnie's Hideaway will always make you feel pampered...</p>

  <div class="service-circle circle-waxing" role="img" aria-label="Woman showing smooth underarm after waxing"></div>
  <div class="service-circle circle-nails" role="img" aria-label="Manicure being applied to a client's hands"></div>
  <div class="service-circle circle-facial" role="img" aria-label="Client receiving a white facial mask"></div>

  <div class="brand-name">Marnie's Hideaway</div>

  <h2 class="open-daily">WE ARE OPEN DAILY</h2>
  <p class="call-in">Call in for special<br>deals at the spa, or<br>visit our website at</p>

  <div class="web-pill">www.marnieshideaway.sg</div>

  <div class="partners">
    <span class="partner" style="left:212px">Veluna Labs</span>
    <span class="partner" style="left:364px">Solenne</span>
    <span class="partner" style="left:474px">Oriane</span>
    <span class="partner" style="left:570px">Elise Marlow</span>
    <span class="partner" style="left:730px">Kirami</span>
  </div>

  <address class="address">Marnie's Hideaway @<br>Larkview<br>88 Larkview<br>Road #02-14<br>Meadow Court<br>Singapore 500123</address>

  <div class="footer-url">www.marnieshideaway.sg</div>
</main>
</body>
</html>
```